TKB Roofing Flyer/Mailer to be used to market to Homeowners

We need to create a flyer than can double as a mailer for our roofing business and possibly be used as a door hanger as well. This flyer will advertise our roofing company in a professional way with pictures as well as clear and precise text about who we are and what we offer. We are open to this flyer being a bi-fold or even a tri-fold. There would need to be an area for address if used as a mailer. A majority of our company information can be found on our website at www.tkbroofing-example.com.

Target Market(s)

Home Owners

Industry/Entity Type

Construction

Colors
0255a3
ffffff

Requirements
Must have
• Professional design, pictures, text with info regarding our company. Website: www.tkbroofing-example.com

```html
<!DOCTYPE html>
<html lang="en">
<head>
<meta charset="utf-8">
<title>TKB Roofing Door Hangers</title>
<link rel="stylesheet" href="https://fonts.googleapis.com/css2?family=Open+Sans:wght@300;400&family=Roboto:wght@400;500&family=Tinos:wght@400;700&display=swap">
<style>
  :root {
    --brand-blue: #0255a3;
    --sky-blue: #1b9ad9;
    --deep-blue: #1d5f9c;
    --ink: #1c1c1e;
    --charcoal: #2f2f31;
    --ring-gray: #5b5b60;
    --soft-gray: #c9c9cc;
    --paper: #ffffff;
    --backdrop: #ecebe8;
  }
  * { margin: 0; padding: 0; box-sizing: border-box; }
  html, body { width: 1058px; height: 1200px; overflow: hidden; }
  body { background: var(--backdrop); position: relative; font-family: "Open Sans", sans-serif; }

  .hanger {
    position: absolute; width: 370px; height: 958px; overflow: hidden;
    box-shadow: 0 6px 18px rgba(0,0,0,.22);
  }
  .hanger--front { left: 145px; top: 85px; }
  .hanger--back { left: 583px; top: 144px; background: linear-gradient(180deg, #ffffff 0%, #f1f1f2 60%, #e6e6e8 100%); }
  .hanger__art { position: absolute; inset: 0; }
  .hanger__text { position: absolute; left: 0; width: 100%; text-align: center; white-space: nowrap; }

  .tagline { top: 14px; font-family: "Tinos", serif; font-weight: 700; font-size: 15px; letter-spacing: 0; }
  .hanger--front .tagline { color: var(--paper); }
  .hanger--back .tagline { color: var(--ink); }

  .brand-seal {
    position: absolute; border-radius: 50%; background: var(--paper);
    border: 6px solid var(--ring-gray); display: flex; align-items: center; justify-content: center;
    box-shadow: 0 3px 8px rgba(0,0,0,.35);
  }
  .brand-seal__name { font-family: "Tinos", serif; font-weight: 700; color: var(--sky-blue); text-align: center; line-height: 1; }
  .hanger--front .brand-seal { left: 104px; top: 459px; width: 166px; height: 166px; }
  .hanger--front .brand-seal__name { font-size: 27px; }
  .hanger--back .brand-seal { left: 126px; top: 405px; width: 118px; height: 118px; }
  .hanger--back .brand-seal__name { font-size: 20px; }

  .service-kicker { top: 645px; color: var(--paper); font-size: 16px; font-weight: 400; }
  .service-title { top: 664px; color: var(--paper); font-family: "Tinos", serif; font-size: 32px; letter-spacing: .3px; }
  .service-copy { top: 710px; left: 24px; width: 322px; color: #e6e6e6; font-size: 11px; line-height: 14.5px; white-space: normal; }

  .call-line { top: 886px; color: var(--paper); font-family: "Tinos", serif; font-weight: 700; font-size: 26px; letter-spacing: .3px; }
  .web-line { top: 922px; color: var(--paper); font-size: 15px; }
  .hanger--back .call-line { top: 884px; }
  .hanger--back .web-line { top: 920px; }

  .question-main { top: 164px; font-size: 40px; font-weight: 300; color: var(--ink); line-height: 50px; }
  .question-sub { top: 208px; font-size: 30px; font-weight: 300; color: var(--ink); line-height: 38px; }
  .accent-mark { color: var(--sky-blue); }
  .investment-note { top: 250px; font-size: 16.5px; font-weight: 300; color: var(--sky-blue); line-height: 20px; }
  .roof-types { top: 307px; font-family: "Roboto", sans-serif; font-size: 16px; color: var(--paper); line-height: 22px; letter-spacing: .2px; }
  .property-note { top: 369px; font-family: "Roboto", sans-serif; font-size: 12.5px; color: var(--sky-blue); line-height: 16px; }
  .services-heading { top: 540px; font-family: "Roboto", sans-serif; font-weight: 500; font-size: 22px; color: var(--paper); }

  .service-list { position: absolute; top: 582px; left: 16px; width: 344px; list-style: none; display: grid; grid-template-columns: 170px 174px; row-gap: 12px; }
  .service-list li { display: flex; align-items: center; gap: 5px; font-family: "Tinos", serif; font-weight: 700; font-size: 12.5px; color: var(--paper); white-space: nowrap; }
  .service-list svg { width: 10px; height: 10px; flex: none; }
</style>
</head>
<body>

<section class="hanger hanger--front">
  <svg class="hanger__art" viewBox="0 0 370 958" width="370" height="958">
    <defs>
      <linearGradient id="front-blue" x1="0" y1="0" x2="1" y2="0">
        <stop offset="0" stop-color="#1b9ad9"/><stop offset="1" stop-color="#1d5a96"/>
      </linearGradient>
      <linearGradient id="front-house" x1="0" y1="0" x2="0" y2="1">
        <stop offset="0" stop-color="#7b8590"/><stop offset=".45" stop-color="#c9c3bb"/><stop offset="1" stop-color="#8f8a82"/>
      </linearGradient>
      <radialGradient id="front-dark" cx=".5" cy=".35" r=".8">
        <stop offset="0" stop-color="#4a4a4d"/><stop offset="1" stop-color="#141415"/>
      </radialGradient>
    </defs>
    <rect width="370" height="958" fill="url(#front-blue)"/>
    <path d="M0,222 Q150,105 370,100" fill="none" stroke="#ffffff" stroke-width="12"/>
    <path d="M0,229 Q150,112 370,106 L370,474 Q260,582 0,584 Z" fill="url(#front-house)" role="img" aria-label="Photo of a brick two-storey home with a grey shingle roof"/>
    <path d="M0,592 Q260,590 370,482 L370,958 L0,958 Z" fill="url(#front-dark)"/>
    <path d="M0,589 Q260,587 370,478" fill="none" stroke="#ffffff" stroke-width="8"/>
    <path d="M0,862 Q185,826 370,862 L370,958 L0,958 Z" fill="url(#front-blue)"/>
    <path d="M0,857 Q185,821 370,857" fill="none" stroke="#ffffff" stroke-width="6"/>
    <circle cx="185" cy="107" r="53" fill="#ecebe8"/>
  </svg>
  <p class="hanger__text tagline">INDY’S PREMIER ROOFING CONTRACTORS</p>
  <div class="brand-seal"><span class="brand-seal__name">TKB Roofing</span></div>
  <p class="hanger__text service-kicker">Residential &amp; Commercial</p>
  <h2 class="hanger__text service-title">ROOFING SERVICES</h2>
  <p class="hanger__text service-copy">By combining high quality products, innovative technologies, and advanced building techniques, we can offer you real workable solutions you can afford. From roof repair and roof replacement, to storm damage restoration, siding work, inspections, and more, our company specializes in several areas of roof types and exterior home renovation, making us your one-stop-shop for all your roofing and siding needs.</p>
  <p class="hanger__text call-line">Call Today! 317-555-0142</p>
  <p class="hanger__text web-line">www.tkbroofing-example.com</p>
</section>

<section class="hanger hanger--back">
  <svg class="hanger__art" viewBox="0 0 370 958" width="370" height="958">
    <defs>
      <linearGradient id="back-shingles" x1="0" y1="0" x2="1" y2="1">
        <stop offset="0" stop-color="#b9825c"/><stop offset=".6" stop-color="#9a6c4e"/><stop offset="1" stop-color="#6d5848"/>
      </linearGradient>
      <linearGradient id="back-dark" x1="0" y1="0" x2="0" y2="1">
        <stop offset="0" stop-color="#3e3e40"/><stop offset="1" stop-color="#18181a"/>
      </linearGradient>
    </defs>
    <rect x="0" y="299" width="370" height="61" fill="var(--ink)"/>
    <path d="M0,444 Q185,484 370,444 L370,958 L0,958 Z" fill="var(--sky-blue)"/>
    <path d="M0,438 Q185,478 370,438" fill="none" stroke="#c9c9cc" stroke-width="8"/>
    <path d="M0,694 Q185,662 370,694 L370,848 L0,848 Z" fill="url(#back-shingles)" role="img" aria-label="Photo of a damaged shingle roof with a ladder against the gutter"/>
    <path d="M0,690 Q185,658 370,690" fill="none" stroke="#ffffff" stroke-width="6"/>
    <path d="M0,848 Q185,820 370,848 L370,958 L0,958 Z" fill="url(#back-dark)"/>
    <path d="M0,844 Q185,816 370,844" fill="none" stroke="#c9c9cc" stroke-width="6"/>
    <circle cx="185" cy="108" r="53" fill="#ecebe8"/>
  </svg>
  <p class="hanger__text tagline">INDY’S PREMIER ROOFING CONTRACTORS</p>
  <h2 class="hanger__text question-main">Shingles curling<span class="accent-mark">?</span></h2>
  <p class="hanger__text question-sub">Have water damage<span class="accent-mark">?</span></p>
  <p class="hanger__text investment-note">Your house is your biggest investment, and<br>your roof is protecting that investment</p>
  <p class="hanger__text roof-types">WHETHER ITS A STEEP ROOF OR A REGULAR<br>PITCHED ROOF WE DO THEM ALL</p>
  <p class="hanger__text property-note">We serve both residential and commercial properties<br>with a wide range of roof repair and installation solutions</p>
  <div class="brand-seal"><span class="brand-seal__name">TKB Roofing</span></div>
  <h3 class="hanger__text services-heading">Our Service Include</h3>
  <ul class="service-list">
    <li><svg viewBox="0 0 10 10"><circle cx="5" cy="5" r="5" fill="#fff"/><path d="M4,2.8 L6.2,5 L4,7.2" fill="none" stroke="#1b9ad9" stroke-width="1.4"/></svg>ROOF REPAIR</li>
    <li><svg viewBox="0 0 10 10"><circle cx="5" cy="5" r="5" fill="#fff"/><path d="M4,2.8 L6.2,5 L4,7.2" fill="none" stroke="#1b9ad9" stroke-width="1.4"/></svg>STORM DAMAGE REPAIR</li>
    <li><svg viewBox="0 0 10 10"><circle cx="5" cy="5" r="5" fill="#fff"/><path d="M4,2.8 L6.2,5 L4,7.2" fill="none" stroke="#1b9ad9" stroke-width="1.4"/></svg>ROOF REPLACEMENT</li>
    <li><svg viewBox="0 0 10 10"><circle cx="5" cy="5" r="5" fill="#fff"/><path d="M4,2.8 L6.2,5 L4,7.2" fill="none" stroke="#1b9ad9" stroke-width="1.4"/></svg>INSURANCE CLAIMS</li>
  </ul>
  <p class="hanger__text call-line">Call Today! 317-555-0142</p>
  <p class="hanger__text web-line">www.tkbroofing-example.com</p>
</section>

</body>
</html>
```